TallPinesCamper.com

Current website needs redesign to make it more attractive and easier to Navigate. Currently being hosted on host harbor. Can be accessed at
www,tallpinescamper.com.

Coding

Coded - Design and coding required

```html
<!DOCTYPE html>
<html lang="en">
<head>
<meta charset="utf-8">
<title>TallPinesCamper.com – Home Page Layouts</title>
<link rel="stylesheet" href="https://fonts.googleapis.com/css2?family=Lexend:wght@500;600&family=Open+Sans:wght@400;600&display=swap">
<style>
:root{
  --backdrop:#898a8b;
  --red:#c8161f;
  --red-deep:#a80f18;
  --ink:#1b1b1b;
  --muted:#555;
  --line:#dcdcdc;
  --black:#050505;
  --white:#fff;
  --step-dark:#474747;
}
*{box-sizing:border-box;margin:0;padding:0}
html,body{width:787px;height:1200px;overflow:hidden}
body{background:var(--backdrop);font-family:"Open Sans",Arial,sans-serif;color:var(--ink)}
.stage{position:absolute;left:0;top:0;width:1562px;height:2380px;transform:scale(.50384);transform-origin:0 0}
.layout{position:absolute;width:660px;background:var(--white);overflow:hidden}
.layout--wave{left:82px;top:100px;height:2180px}
.layout--flat{left:820px;top:100px;height:1948px}
.shapes{position:absolute;left:0;top:0}

/* navigation */
.nav{position:absolute;left:0;top:28px;width:660px;height:40px;background:var(--white);border-radius:6px;z-index:3}
.nav a{position:absolute;top:14px;font-size:8px;color:var(--ink);text-decoration:none;white-space:nowrap}
.nav .nav-cta{top:8px;left:541px;width:78px;height:24px;border-radius:12px;background:var(--red);color:var(--white);font-family:"Lexend",sans-serif;font-weight:500;text-align:center;line-height:24px}
.brand-badge{position:absolute;left:297px;top:17px;width:66px;height:66px;border-radius:50%;background:var(--white);z-index:4;text-align:center}
.brand-badge .dot{display:block;width:12px;height:12px;border-radius:50%;background:var(--red);margin:14px auto 3px}
.brand-badge .name{font-family:"Lexend",sans-serif;font-weight:600;font-size:8px;color:var(--ink);line-height:9px}

/* hero */
.hero{position:absolute;left:0;top:0;width:660px;background:linear-gradient(180deg,#6f7479 0%,#7c7a62 22%,#c19b1f 38%,#d3a81f 52%,#9b7b18 66%,#2b2b2b 82%,#151515 100%)}
.hero-copy{position:absolute;left:0;top:152px;width:660px;text-align:center;color:var(--white);z-index:2}
.hero-title{font-family:"Lexend",sans-serif;font-weight:600;font-size:25px;letter-spacing:.2px}
.hero-text{font-size:8px;line-height:14px;margin-top:10px}
.pill{display:inline-block;height:30px;line-height:30px;padding:0 16px;border-radius:15px;font-family:"Lexend",sans-serif;font-weight:500;font-size:8px}
.pill--red{background:var(--red);color:var(--white)}
.pill--white{background:var(--white);color:var(--red)}
.hero-copy .pill{margin-top:14px}
.dots{position:absolute;left:291px;top:306px;display:flex;gap:3px;z-index:2}
.dots i{width:7px;height:7px;border-radius:50%;background:var(--white)}
.dots i.on{background:transparent;border:1px solid var(--white)}

/* about */
.about-mark{position:absolute;left:60px;width:270px;height:240px;text-align:center}
.about-mark .disc{width:150px;height:150px;border-radius:50%;background:var(--red);margin:20px auto 14px}
.about-mark .name{font-family:"Lexend",sans-serif;font-weight:600;font-size:20px;color:var(--red)}
.section-title{font-family:"Lexend",sans-serif;font-weight:600;font-size:18px;color:var(--ink)}
.about-copy{position:absolute;left:355px;width:250px}
.about-copy p{font-size:7.6px;line-height:14.2px;color:var(--muted);margin:12px 0 20px}

/* mission */
.mission-block{position:absolute;left:0;width:660px;background:linear-gradient(160deg,#b40f19 0%,#cf1c26 55%,#b8121b 100%)}
.mission-copy{position:absolute;left:95px;width:470px;text-align:center;color:var(--white);z-index:2}
.mission-copy .section-title{color:var(--white)}
.mission-copy p{font-size:7.6px;line-height:14.2px;margin:12px 0 16px}

/* blog */
.blog-title{position:absolute;left:0;width:660px;text-align:center}
.blog-grid{position:absolute;left:60px;display:grid;grid-template-columns:262px 262px;column-gap:14px;row-gap:11px}
.post{position:relative;height:150px;background:var(--white);border-radius:4px;box-shadow:0 1px 6px rgba(0,0,0,.18);overflow:hidden}
.post-photo{position:absolute;left:0;top:0;width:118px;height:150px}
.post-body{position:absolute;left:128px;top:6px;width:124px}
.post-title{font-family:"Lexend",sans-serif;font-weight:600;font-size:10.5px;line-height:16px}
.post-date{font-size:7.6px;color:var(--red);margin:3px 0 7px}
.post-text{font-size:7.4px;line-height:14px;color:#333}
.post-link{font-size:7.6px;color:var(--red);text-decoration:underline;font-weight:600}
.photo--coach{background:linear-gradient(160deg,#9aa3ad 0%,#5e5650 45%,#3d342e 75%,#8a8378 100%)}
.photo--sunset{background:linear-gradient(180deg,#3b2b2a 0%,#d8702a 40%,#5b4a3b 55%,#7b7166 100%)}
.photo--night{background:linear-gradient(180deg,#0e1a3b 0%,#1d2c55 45%,#c7c9cc 70%,#4a4a4a 100%)}
.photo--street{background:linear-gradient(180deg,#7fa6cf 0%,#b9c6a8 45%,#6e6c6a 75%,#4f4d4b 100%)}

/* contact */
.contact{position:absolute;left:62px;width:538px;height:261px;background:var(--white);box-shadow:0 1px 6px rgba(0,0,0,.16)}
.contact-photo{position:absolute;left:0;top:0;width:187px;height:261px;background:linear-gradient(180deg,#c9cdd1 0%,#a7a49f 30%,#4a3b35 55%,#2e2724 72%,#8c8274 88%,#b3aa98 100%)}
.contact-body{position:absolute;left:205px;top:28px;width:310px}
.contact-body .section-title{font-size:19px;letter-spacing:.5px}
.contact-lead{font-size:7.6px;color:#333;margin:12px 0 12px 2px}
.steps{position:relative;display:inline-flex;gap:25px;margin-left:2px;height:24px}
.steps::before{content:"";position:absolute;left:12px;right:12px;top:12px;height:1px;background:#999}
.step{position:relative;width:24px;height:24px;border-radius:50%;background:var(--step-dark);color:var(--white);font-size:8px;text-align:center;line-height:20px;border:2px solid #ececec}
.step--on{background:var(--red)}
.fields{display:grid;grid-template-columns:147px 147px;column-gap:13px;row-gap:12px;margin:8px 0 0 2px}
.field{height:25px;border:1px solid var(--line);font-size:7.6px;color:#888;padding-left:9px;line-height:23px;letter-spacing:.3px}
.submit{display:inline-flex;align-items:center;gap:5px;margin:18px 0 0 5px;height:23px;padding:0 13px;border-radius:12px;background:var(--red);color:var(--white);font-family:"Lexend",sans-serif;font-weight:600;font-size:7.6px;letter-spacing:.4px}

/* footer */
.footer-block{position:absolute;left:0;width:660px;background:var(--black)}
.foot{position:absolute;left:0;width:660px;color:var(--white);z-index:2}
.foot-brand{position:absolute;left:60px;top:28px;display:flex;align-items:center;gap:5px}
.foot-brand .dot{width:12px;height:12px;border-radius:50%;background:var(--red)}
.foot-brand .name{font-family:"Lexend",sans-serif;font-weight:600;font-size:13px;color:var(--white)}
.foot-col{position:absolute;top:0}
.foot-col h4{font-family:"Lexend",sans-serif;font-weight:600;font-size:9.5px;letter-spacing:.6px;margin-bottom:6px}
.foot-col li{list-style:none;font-size:7.6px;line-height:14.2px}
.subscribe{width:120px;height:16px;border-bottom:1px solid #bbb;display:flex;align-items:center;gap:4px;font-size:7.6px;color:#aaa;position:relative}
.subscribe .send{position:absolute;right:2px;top:3px}
.socials{display:flex;gap:5px;margin-top:14px}
.socials i{width:6px;height:6px;border-radius:50%;background:var(--white)}
.foot-rule{position:absolute;left:60px;width:540px;height:1px;background:#222}
.copyright{position:absolute;left:0;width:660px;text-align:center;font-size:7.6px}
</style>
</head>
<body>
<div class="stage">

<section class="layout layout--wave">
  <div class="hero" style="height:470px" role="img" aria-label="Photo of a yellow camper van driving on a highway under a cloudy sky"></div>

  <svg class="shapes" width="660" height="2180" viewBox="0 0 660 2180" aria-hidden="true">
    <defs>
      <linearGradient id="missionRed" x1="0" y1="0" x2="1" y2="1">
        <stop offset="0" stop-color="#b40f19"/><stop offset=".55" stop-color="#d01d27"/><stop offset="1" stop-color="#b5111a"/>
      </linearGradient>
    </defs>
    <path fill="#fff" d="M0 440 C40 385 85 380 135 395 C200 415 235 345 330 345 C425 345 455 400 530 392 C600 385 640 410 660 440 L660 480 L0 480 Z"/>
    <path fill="url(#missionRed)" d="M0 740 C60 800 110 860 200 850 C290 840 330 780 430 800 C520 820 560 780 660 740 L660 1140 C600 1110 560 1060 480 1080 C400 1100 360 1050 260 1040 C170 1035 110 1100 0 1140 Z"/>
    <path fill="#050505" d="M0 1860 C40 1930 120 1890 200 1940 C260 1975 320 1975 380 1950 C460 1910 560 1960 660 1860 L660 2180 L0 2180 Z"/>
  </svg>

  <nav class="nav">
    <a style="left:42px">About</a><a style="left:87px">Trails &amp; Tales</a><a style="left:160px">The Smart Rer</a><a style="left:236px">Bad RV</a>
    <a style="left:391px">Women on the Road</a><a style="left:490px">Blog</a><a class="nav-cta">Contact US</a>
  </nav>
  <div class="brand-badge"><span class="dot"></span><div class="name">TallPines<br>Camper.com</div></div>

  <div class="hero-copy">
    <h1 class="hero-title">Welcome To Tall Pines</h1>
    <p class="hero-text">Lorem ipsum dolor sit amet, consectetur adipiscing elit, sed do eiusmod<br>tempor incididunt ut labore et dolore magna aliqua.</p>
    <span class="pill pill--red">Learn More</span>
  </div>
  <div class="dots"><i></i><i></i><i class="on"></i><i></i><i></i></div>

  <div class="about-mark" style="top:460px"><div class="disc"></div><div class="name">TallPinesCamper.com</div></div>
  <div class="about-copy" style="top:484px">
    <h2 class="section-title">About Us</h2>
    <p>Lorem ipsum dolor sit amet, consectetur adipiscing elit, sed do eiusmod tempor incididunt ut labore et dolore magna aliqua. Quis ipsum suspendisse ultrices gravida. Risus commodo viverra maecenas accumsan lacus vel facilisis. Lorem ipsum dolor sit amet, consectetur adipiscing elit, sed do eiusmod tempor incididunt ut labore et dolore magna aliqua. Quis ipsum suspendisse ultrices gravida. Risus commodo viverra maecenas accumsan lacus vel facilisis.</p>
    <span class="pill pill--red">Learn More</span>
  </div>

  <div class="mission-copy" style="top:864px;left:85px">
    <h2 class="section-title">Our Mission</h2>
    <p>Our mission is to help new and veteran RVers smooth out the bumps in the road that are inherent in RV ownership. We are primarily an educational and advisory website dedicated to helping other RVers make less mistakes and take fewer missteps on their journey to adventure. Our Smart RVer section is dedicated to giving our readers tips and advice on making the Rv journey an easier one. We will use the “wisdom of the crowd”, namely you our readers, to provide much of the content for this section.</p>
    <span class="pill pill--white">Learn More</span>
  </div>

  <h2 class="section-title blog-title" style="top:1177px">Featured Blog Posts</h2>
  <div class="blog-grid" style="top:1222px">
    <article class="post"><div class="post-photo photo--coach" role="img" aria-label="Photo of a large motorhome parked in a lot"></div>
      <div class="post-body"><h3 class="post-title">Bad RV</h3><div class="post-date">Dec 11, 2021</div><p class="post-text">We serve as an advocacy forum for other RVers seeking advice and remediation against both dealers and manufacturers who fail to meet their customer obligations.</p><span class="post-link">Learn More</span></div></article>
    <article class="post"><div class="post-photo photo--sunset" role="img" aria-label="Photo of an empty desert road at sunset"></div>
      <div class="post-body"><h3 class="post-title">RV Envy? Why you will always want a different one!</h3><div class="post-date">Dec 11, 2021</div><p class="post-text">We serve as an advocacy forum for other RVers seeking advice and remediation against both dealers.</p><span class="post-link">Learn More</span></div></article>
    <article class="post"><div class="post-photo photo--night" role="img" aria-label="Photo of a class C motorhome under a starry night sky"></div>
      <div class="post-body"><h3 class="post-title">Class A Motorhomes: Prepare for a love hate relationship</h3><div class="post-date">Dec 11, 2021</div><p class="post-text">My wife and I have owned two class A motorhomes: one a new 37 ft. gas coach and a new 40 ft.bath and half diesel pusher.</p><span class="post-link">Learn More</span></div></article>
    <article class="post"><div class="post-photo photo--street" role="img" aria-label="Photo of a campground street with a folding chair"></div>
      <div class="post-body"><h3 class="post-title">RV Hell: Driving off without your wife!</h3><div class="post-date">Dec 11, 2021</div><p class="post-text">It was a steady downpour that day in rural Mississippi. We were on a four-lane highway in our Dunewick 36 FK towing our dozer yellow Brambleton 4x4.</p><span class="post-link">Learn More</span></div></article>
  </div>

  <div class="contact" style="top:1581px">
    <div class="contact-photo" role="img" aria-label="Photo of a dark motorhome parked on gravel"></div>
    <div class="contact-body">
      <h2 class="section-title">Contact Us</h2>
      <p class="contact-lead">Lorem ipsum dolor sit amet, consectetur adipiscing elit,</p>
      <div class="steps"><span class="step step--on">1</span><span class="step">2</span><span class="step">3</span></div>
      <div class="fields"><div class="field">First Name</div><div class="field">Last Name</div><div class="field">Phone Number</div><div class="field">Email</div></div>
      <span class="submit">SUBMIT <svg width="8" height="8" viewBox="0 0 8 8"><circle cx="4" cy="4" r="3.6" fill="#fff"/><path d="M2.3 4h3M4.1 2.7 5.4 4 4.1 5.3" stroke="#c8161f" stroke-width=".9" fill="none"/></svg></span>
    </div>
  </div>

  <footer class="foot" style="top:1993px">
    <div class="foot-brand"><span class="dot"></span><span class="name">TallPinesCamper.com</span></div>
    <div class="foot-col" style="left:237px"><h4>Quick link</h4><ul><li>About</li><li>Trails &amp; Tales</li><li>The Smart Rer</li><li>Bad RV</li><li>Women on the Road</li><li>Blog</li><li>Contctus</li></ul></div>
    <div class="foot-col" style="left:353px"><h4>Help link</h4><ul><li>Terms &amp; Conditions</li><li>Privacy Policy</li><li>Terms of Sales</li></ul></div>
    <div class="foot-col" style="left:479px"><h4>Subscribe</h4>
      <div class="subscribe"><svg width="8" height="6" viewBox="0 0 8 6"><rect x=".4" y=".4" width="7.2" height="5.2" fill="none" stroke="#aaa" stroke-width=".7"/><path d="M.5.6 4 3.3 7.5.6" fill="none" stroke="#aaa" stroke-width=".7"/></svg>Email<svg class="send" width="7" height="7" viewBox="0 0 7 7"><path d="M.5 3.5 6.5.5 5 6.5 3.5 4Z" fill="none" stroke="#c8161f" stroke-width=".7"/></svg></div>
      <div class="socials"><i></i><i></i><i></i><i></i></div>
    </div>
    <div class="foot-rule" style="top:137px"></div>
    <p class="copyright" style="top:156px;left:-18px">©Copyrights 2021 Company Name &nbsp;| &nbsp; All Rights Reserved</p>
  </footer>
</section>

<section class="layout layout--flat">
  <div class="hero" style="height:371px" role="img" aria-label="Photo of a yellow camper van driving on a highway under a cloudy sky"></div>

  <nav class="nav">
    <a style="left:42px">About</a><a style="left:87px">Trails &amp; Tales</a><a style="left:160px">The Smart Rer</a><a style="left:236px">Bad RV</a>
    <a style="left:391px">Women on the Road</a><a style="left:490px">Blog</a><a class="nav-cta">Contact US</a>
  </nav>
  <div class="brand-badge"><span class="dot"></span><div class="name">TallPines<br>Camper.com</div></div>

  <div class="hero-copy">
    <h1 class="hero-title">Welcome To Tall Pines</h1>
    <p class="hero-text">Lorem ipsum dolor sit amet, consectetur adipiscing elit, sed do eiusmod<br>tempor incididunt ut labore et dolore magna aliqua.</p>
    <span class="pill pill--red">Learn More</span>
  </div>
  <div class="dots"><i></i><i></i><i class="on"></i><i></i><i></i></div>

  <div class="about-mark" style="top:410px"><div class="disc"></div><div class="name">TallPinesCamper.com</div></div>
  <div class="about-copy" style="top:433px">
    <h2 class="section-title">About Us</h2>
    <p>Lorem ipsum dolor sit amet, consectetur adipiscing elit, sed do eiusmod tempor incididunt ut labore et dolore magna aliqua. Quis ipsum suspendisse ultrices gravida. Risus commodo viverra maecenas accumsan lacus vel facilisis. Lorem ipsum dolor sit amet, consectetur adipiscing elit, sed do eiusmod tempor incididunt ut labore et dolore magna aliqua. Quis ipsum suspendisse ultrices gravida. Risus commodo viverra maecenas accumsan lacus vel facilisis.</p>
    <span class="pill pill--red">Learn More</span>
  </div>

  <div class="mission-block" style="top:695px;height:260px"></div>
  <div class="mission-copy" style="top:747px">
    <h2 class="section-title">Our Mission</h2>
    <p>Our mission is to help new and veteran RVers smooth out the bumps in the road that are inherent in RV ownership. We are primarily an educational and advisory website dedicated to helping other RVers make less mistakes and take fewer missteps on their journey to adventure. Our Smart RVer section is dedicated to giving our readers tips and advice on making the Rv journey an easier one. We will use the “wisdom of the crowd”, namely you our readers, to provide much of the content for this section.</p>
    <span class="pill pill--white">Learn More</span>
  </div>

  <h2 class="section-title blog-title" style="top:1001px">Featured Blog Posts</h2>
  <div class="blog-grid" style="top:1045px">
    <article class="post"><div class="post-photo photo--coach" role="img" aria-label="Photo of a large motorhome parked in a lot"></div>
      <div class="post-body"><h3 class="post-title">Bad RV</h3><div class="post-date">Dec 11, 2021</div><p class="post-text">We serve as an advocacy forum for other RVers seeking advice and remediation against both dealers and manufacturers who fail to meet their customer obligations.</p><span class="post-link">Learn More</span></div></article>
    <article class="post"><div class="post-photo photo--sunset" role="img" aria-label="Photo of an empty desert road at sunset"></div>
      <div class="post-body"><h3 class="post-title">RV Envy? Why you will always want a different one!</h3><div class="post-date">Dec 11, 2021</div><p class="post-text">We serve as an advocacy forum for other RVers seeking advice and remediation against both dealers.</p><span class="post-link">Learn More</span></div></article>
    <article class="post"><div class="post-photo photo--night" role="img" aria-label="Photo of a class C motorhome under a starry night sky"></div>
      <div class="post-body"><h3 class="post-title">Class A Motorhomes: Prepare for a love hate relationship</h3><div class="post-date">Dec 11, 2021</div><p class="post-text">My wife and I have owned two class A motorhomes: one a new 37 ft. gas coach and a new 40 ft.bath and half diesel pusher.</p><span class="post-link">Learn More</span></div></article>
    <article class="post"><div class="post-photo photo--street" role="img" aria-label="Photo of a campground street with a folding chair"></div>
      <div class="post-body"><h3 class="post-title">RV Hell: Driving off without your wife!</h3><div class="post-date">Dec 11, 2021</div><p class="post-text">It was a steady downpour that day in rural Mississippi. We were on a four-lane highway in our Dunewick 36 FK towing our dozer yellow Brambleton 4x4.</p><span class="post-link">Learn More</span></div></article>
  </div>

  <div class="contact" style="top:1405px">
    <div class="contact-photo" role="img" aria-label="Photo of a dark motorhome parked on gravel"></div>
    <div class="contact-body">
      <h2 class="section-title">Contact Us</h2>
      <p class="contact-lead">Lorem ipsum dolor sit amet, consectetur adipiscing elit,</p>
      <div class="steps"><span class="step step--on">1</span><span class="step">2</span><span class="step">3</span></div>
      <div class="fields"><div class="field">First Name</div><div class="field">Last Name</div><div class="field">Phone Number</div><div class="field">Email</div></div>
      <span class="submit">SUBMIT <svg width="8" height="8" viewBox="0 0 8 8"><circle cx="4" cy="4" r="3.6" fill="#fff"/><path d="M2.3 4h3M4.1 2.7 5.4 4 4.1 5.3" stroke="#c8161f" stroke-width=".9" fill="none"/></svg></span>
    </div>
  </div>

  <div class="footer-block" style="top:1716px;height:232px"></div>
  <footer class="foot" style="top:1747px">
    <div class="foot-brand" style="top:40px"><span class="dot"></span><span class="name">TallPinesCamper.com</span></div>
    <div class="foot-col" style="left:237px"><h4>Quick link</h4><ul><li>About</li><li>Trails &amp; Tales</li><li>The Smart Rer</li><li>Bad RV</li><li>Women on the Road</li><li>Blog</li><li>Contctus</li></ul></div>
    <div class="foot-col" style="left:353px"><h4>Help link</h4><ul><li>Terms &amp; Conditions</li><li>Privacy Policy</li><li>Terms of Sales</li></ul></div>
    <div class="foot-col" style="left:479px"><h4>Subscribe</h4>
      <div class="subscribe"><svg width="8" height="6" viewBox="0 0 8 6"><rect x=".4" y=".4" width="7.2" height="5.2" fill="none" stroke="#aaa" stroke-width=".7"/><path d="M.5.6 4 3.3 7.5.6" fill="none" stroke="#aaa" stroke-width=".7"/></svg>Email<svg class="send" width="7" height="7" viewBox="0 0 7 7"><path d="M.5 3.5 6.5.5 5 6.5 3.5 4Z" fill="none" stroke="#c8161f" stroke-width=".7"/></svg></div>
      <div class="socials"><i></i><i></i><i></i><i></i></div>
    </div>
    <p class="copyright" style="top:161px;left:-18px">©Copyrights 2021 Company Name &nbsp;| &nbsp; All Rights Reserved</p>
  </footer>
</section>

</div>
</body>
</html>
```